European Indian Investment firm

I would like to have a complete make-over of an existing website. Have a look at : www.velmoranpartners-example.com
We are a European/Indian based investment firm that acquires stakes in European (Manufacturing) companies (industrial) and help them grow in India. We have a team in Europe (Barcelona, Zurich, Amsterdam) and in India (Bangalore).
Amongst the new lay-out of the website also the name and the logo of the site will change. I will upload the new company logo. The new site should broadly send out the same message which is bridging Europe and India and also it should have an industrial/manufacturing look. The wording and the various pages of the website will be broadly the same as the old one with some changes which we will provide further down the road. I

Target Market(s)

Europe and India. Entrepreneurs, CEO's and investors.

Industry/Entity Type

Investment

Coding

Coded - Design and coding required

Number of Pages Required

5+ page

Font styles to use
Sans Serif

Requirements
Must have
• site should have an industrial look and also it should reflect the bridging between the two continents Europe and India provided by the team helping companies to grow.

```html
<!DOCTYPE html>
<html lang="en">
<head>
<meta charset="utf-8">
<title>Velmoran Partners</title>
<link href="https://fonts.googleapis.com/css2?family=Open+Sans:wght@400;600;700&display=swap" rel="stylesheet">
<style>
:root{
  --teal:#2f4a52;
  --teal-dark:#243a41;
  --orange:#c8632a;
  --ink:#2b2b2b;
  --muted:#6d6d6d;
  --stone:#a7998a;
  --line:#c9c9c9;
  --footer:#2a2d30;
  --footer-bar:#1f2224;
  --white:#fff;
}
*{box-sizing:border-box;margin:0;padding:0}
html,body{width:683px;height:1200px;overflow:hidden}
body{font-family:"Open Sans",Arial,sans-serif;color:var(--ink);background:var(--white);font-size:8px;line-height:1.5}
.page{width:683px;height:1200px;position:relative}

.topbar{height:44px;display:flex;align-items:center;justify-content:space-between;padding:0 40px}
.brand{display:flex;align-items:center;gap:6px;font-weight:700;font-size:12px;color:var(--teal)}
.brand-mark{width:14px;height:14px;background:var(--teal)}
.contact-strip{display:flex;align-items:center;gap:10px;font-size:7.5px;color:var(--muted)}
.contact-strip span{display:flex;align-items:center;gap:3px}
.social{display:flex;gap:3px}
.social i{width:11px;height:11px;background:var(--teal);display:block}

.nav{height:16px;background:var(--teal);display:flex;justify-content:center;gap:0}
.nav a{color:var(--white);text-decoration:none;font-size:6.5px;letter-spacing:.5px;font-weight:600;padding:0 18px;line-height:16px}
.nav a.active{background:var(--orange)}

.hero{height:210px;position:relative;background:linear-gradient(180deg,#4a5a62 0%,#3a4850 60%,#2e3a40 100%);color:var(--white);padding:34px 40px}
.hero h1{font-size:20px;font-weight:700;line-height:1.2}
.hero .tag{display:inline-block;background:var(--orange);font-size:7px;padding:1px 6px;margin:6px 0 6px}
.hero p{font-size:7px;max-width:240px;opacity:.9}
.btn{display:inline-block;background:var(--orange);color:var(--white);font-size:6.5px;font-weight:700;letter-spacing:.4px;padding:5px 12px;text-transform:uppercase}
.hero .btn{margin-top:10px}

.intro{text-align:center;padding:26px 110px 0;font-size:7.5px;color:var(--muted)}

.services{text-align:center;margin-top:26px}
.gears{width:70px;height:58px;margin:0 auto;border-radius:50%;background:radial-gradient(circle,#2f4a52 0%,#3d5b63 60%,#e9eced 61%)}
h2{font-size:14px;font-weight:600;color:var(--ink)}
.services h2{margin-top:10px}
.sub{font-size:7px;color:var(--muted);margin-top:2px}
.btn-dark{background:var(--teal);margin-top:12px}
.tree{display:block;margin:0 auto}
.sectors{display:flex;justify-content:center;gap:0;padding:0 56px}
.sector{width:81px;text-align:center;font-size:6.5px;color:var(--ink);line-height:1.3}
.sector .dot{width:30px;height:30px;border-radius:50%;background:var(--stone);margin:0 auto 5px;display:flex;align-items:center;justify-content:center}
.sector .dot i{width:12px;height:10px;border:1.5px solid var(--white);display:block}

.portfolio{text-align:center;margin-top:40px}
.tiles{display:flex;gap:8px;justify-content:center;margin-top:16px}
.tile{width:194px;height:110px;position:relative}
.tile figcaption{position:absolute;left:0;right:0;bottom:0;background:rgba(40,55,60,.75);color:var(--white);font-size:6.5px;text-align:left;padding:3px 6px}
.t1{background:linear-gradient(135deg,#8a9aa2,#5f6e75)}
.t2{background:linear-gradient(135deg,#2c3f66,#d9a04a 55%,#2a3552)}
.t3{background:linear-gradient(135deg,#3c6a5e,#9fc6b6)}

.cta{position:absolute;top:832px;left:0;width:683px;height:92px;background:linear-gradient(180deg,#353b3f,#2a2f33);color:var(--white);text-align:center;padding-top:18px}
.cta h2{color:var(--white);font-size:13px}
.cta p{font-size:7px;opacity:.8;margin:3px 0 8px}

.footer{position:absolute;top:924px;left:0;width:683px;height:256px;background:var(--footer);color:#cfd3d5;display:flex;gap:30px;padding:26px 40px}
.col{flex:1}
.col h3{font-size:8px;color:var(--white);font-weight:600;margin-bottom:8px}
.col li{list-style:none;font-size:6.5px;margin-bottom:5px}
.contact-item{display:flex;gap:6px;align-items:flex-start;font-size:6.5px;margin-bottom:8px}
.contact-item b{width:12px;height:12px;border-radius:50%;background:var(--teal);flex:none}
.field{height:12px;background:#41464a;margin-bottom:5px;font-size:6px;padding:2px 4px;color:#999}
.btn-small{font-size:6px;padding:3px 8px}
.bottom{position:absolute;top:1180px;left:0;width:683px;height:20px;background:var(--footer-bar);color:#9aa0a3;font-size:6px;display:flex;align-items:center;justify-content:space-between;padding:0 40px}
.bottom .social i{width:9px;height:9px;background:#4a5358}
</style>
</head>
<body>
<div class="page">
  <header class="topbar">
    <div class="brand"><span class="brand-mark"></span>Velmoran Partners</div>
    <div class="contact-strip">
      <span>
        <svg width="8" height="8" viewBox="0 0 10 10"><path d="M2 1l2 2-1 1.5c.8 1.5 1.7 2.4 3 3L7.5 6l2 2-1.5 1.5C4.5 9 1 5.5.5 2.5z" fill="#2f4a52"/></svg>
        +(00) 20 555 0142</span>
      <span>
        <svg width="8" height="8" viewBox="0 0 10 10"><circle cx="5" cy="5" r="4" fill="none" stroke="#2f4a52"/><path d="M1 5h8M5 1v8" stroke="#2f4a52" stroke-width=".8"/></svg>
        www.velmoranpartners-example.com</span>
      <div class="social"><i></i><i></i><i></i></div>
    </div>
  </header>
  <nav class="nav">
    <a class="active">APPROACH</a><a>STRENGTH</a><a>TEAM</a><a>PORTFOLIO</a><a>PUBLICATIONS</a><a>INVESTORS</a><a>CONTACT</a>
  </nav>

  <section class="hero" role="img" aria-label="Industrial machinery photograph behind headline">
    <h1>Building truly global European industrial SMEs</h1>
    <span class="tag">European Indian investment firm</span>
    <p>We are a European Indian based investment firm that acquires stakes in European industrial companies and helps them grow in India.</p>
    <span class="btn">How to get started guide</span>
  </section>

  <p class="intro">Velmoran Partners is a Euro-Indian partnership that invests in European industrial SMEs that face a growth challenge. We acquire controlling stakes in businesses facing "special situations", either underperformance, stress, distress or right-out insolvency. Our target companies are basic processing and manufacturing industries, a segment of industry that is mostly facing flat or declining home markets. We also team up with European industrial groups to set up stand-alone Joint Ventures to develop the Indian market.</p>

  <section class="services">
    <div class="gears" role="img" aria-label="Gears and cogs illustration"></div>
    <h2>Our Services</h2>
    <p class="sub">Our target companies are operating in the EU* old economies*</p>
    <span class="btn btn-dark">Find out more</span>
    <svg class="tree" width="571" height="34" viewBox="0 0 571 34">
      <g stroke="#c9c9c9" stroke-width="1" fill="none">
        <path d="M285.5 0v12M40.5 12h490M40.5 12v22M121.5 12v22M202.5 12v22M285.5 12v22M366.5 12v22M449.5 12v22M530.5 12v22"/>
      </g>
    </svg>
    <div class="sectors">
      <div class="sector"><div class="dot"><i></i></div>Infrastructure &amp; Construction</div>
      <div class="sector"><div class="dot"><i></i></div>Automotive &amp; Transport</div>
      <div class="sector"><div class="dot"><i></i></div>Engineered Products</div>
      <div class="sector"><div class="dot"><i></i></div>Advanced Materials</div>
      <div class="sector"><div class="dot"><i></i></div>Consumer Goods &amp; Retail</div>
      <div class="sector"><div class="dot"><i></i></div>Basic process Industries</div>
      <div class="sector"><div class="dot"><i></i></div>Healthcare</div>
    </div>
  </section>

  <section class="portfolio">
    <h2>Our Portfolio</h2>
    <div class="tiles">
      <figure class="tile t1" role="img" aria-label="Robotic arm on a production line"><figcaption>Sample portfolio title 01 here</figcaption></figure>
      <figure class="tile t2" role="img" aria-label="Welding sparks in a metal workshop"><figcaption>Sample portfolio title 02 here</figcaption></figure>
      <figure class="tile t3" role="img" aria-label="Green industrial heat exchanger fins"><figcaption>Sample portfolio title 03 here</figcaption></figure>
    </div>
  </section>

  <section class="cta">
    <h2>How do I get started?</h2>
    <p>Click button below to Request a Quote. I will have a document on my letterhead with required information.</p>
    <span class="btn">How to get started guide</span>
  </section>

  <footer class="footer">
    <div class="col">
      <h3>Main menu</h3>
      <ul><li>Home</li><li>Services</li><li>Portfolio</li><li>Team</li><li>Contact Us</li></ul>
    </div>
    <div class="col">
      <h3>Information</h3>
      <ul><li>Policies</li><li>Legal Notes</li><li>Terms and conditions of use</li><li>Announcements</li><li>Publications</li><li>News</li></ul>
    </div>
    <div class="col">
      <h3>Contact us</h3>
      <div class="contact-item"><b></b><span>12 Harbour Street, Suite 4<br>Amsterdam 1000 AA</span></div>
      <div class="contact-item"><b></b><span>+(00) 20 555 0142</span></div>
      <div class="contact-item"><b></b><span>info@velmoranpartners-example.com</span></div>
    </div>
    <div class="col">
      <h3>Newsletter</h3>
      <div class="field">Your name</div>
      <div class="field">Your email</div>
      <span class="btn btn-small">Submit</span>
    </div>
  </footer>
  <div class="bottom">
    <span>© 2024 Velmoran Partners Investment Firm</span>
    <div class="social"><i></i><i></i><i></i></div>
  </div>
</div>
</body>
</html>
```